KLOMB Systems website

We need a website design using much of the information on the KLOMB flyer (attached) we just had a PixelBarn designer create. We'd like a WordPress Site, no need for a shopping cart attached to it. It should have an About us page, Book titles page, a blog page, Membership and Navigators pages contact us and privacy policy and terms of services.

```html
<!DOCTYPE html>
<html lang="en">
<head>
<meta charset="utf-8">
<title>KLOMB Systems</title>
<link href="https://fonts.googleapis.com/css2?family=Open+Sans:wght@400;600;700;800&display=swap" rel="stylesheet">
<style>
:root{
  --navy:#1c3d73;
  --navy-dark:#142d58;
  --blue:#2f8fd8;
  --green:#2c9a5a;
  --orange:#f07b22;
  --orange-dark:#e2611a;
  --ink:#3a3f47;
  --muted:#6d7480;
  --line:#e3e6ea;
  --white:#ffffff;
}
*{box-sizing:border-box;margin:0;padding:0}
html,body{width:1200px;height:2856px;overflow:hidden}
body{font-family:"Open Sans",Arial,sans-serif;color:var(--ink);background:var(--white)}
a{color:inherit;text-decoration:none}

/* Header */
.site-header{height:110px;display:flex;align-items:center;justify-content:space-between;padding:0 120px 0 130px;background:var(--white)}
.brand{display:flex;align-items:center;gap:12px;font-weight:800;font-size:34px;color:var(--navy);letter-spacing:1px}
.brand-dot{width:26px;height:26px;border-radius:50%;background:var(--navy)}
.main-nav{display:flex;gap:34px;font-size:13px;font-weight:600;text-transform:uppercase;color:var(--ink)}
.main-nav .active{color:var(--blue)}

/* Hero */
.hero{position:relative;height:530px;display:flex;flex-direction:column;align-items:center;justify-content:center;text-align:center;color:var(--white)}
.hero-photo{position:absolute;inset:0;background:radial-gradient(ellipse at 60% 40%,#5b6470 0%,#333a44 45%,#1b1f26 100%)}
.hero-content{position:relative}
.hero h1{font-size:46px;font-weight:700;line-height:1.15;text-transform:uppercase;letter-spacing:.5px}
.btn{display:inline-block;margin-top:22px;padding:10px 26px;border:2px solid var(--white);color:var(--white);font-size:13px;font-weight:700;text-transform:uppercase;letter-spacing:1px}

/* About */
.about{height:660px;padding-top:56px;text-align:center}
.about-mark{width:40px;height:40px;border-radius:50%;background:var(--navy);margin:0 auto 14px;opacity:.75}
.section-title{font-size:34px;font-weight:800;color:var(--navy);text-transform:uppercase;letter-spacing:1px}
.about-intro{width:760px;margin:18px auto 0;font-size:15px;line-height:1.6;color:var(--muted)}
.pillars{display:flex;justify-content:center;gap:26px;margin-top:92px}
.pillar{position:relative;width:300px;height:300px;padding:64px 28px 20px;background:var(--white);box-shadow:0 2px 14px rgba(0,0,0,.13);border-top:4px solid var(--c)}
.pillar-icon{position:absolute;top:-46px;left:50%;transform:translateX(-50%)}
.pillar h3{font-size:20px;font-weight:800;color:var(--c);text-transform:uppercase;margin-bottom:12px}
.pillar p{font-size:12.5px;line-height:1.5;color:var(--muted);margin-bottom:8px}
.coaching{--c:var(--blue)}
.structure{--c:var(--green)}
.resources{--c:var(--orange)}

/* Why */
.why{height:580px;background:linear-gradient(160deg,#2a5aa0 0%,var(--navy) 50%,var(--navy-dark) 100%);color:var(--white);text-align:center;padding-top:52px}
.why .section-title{color:var(--white)}
.why-grid{display:grid;grid-template-columns:440px 440px;gap:44px 60px;justify-content:center;margin-top:44px;text-align:left}
.why-item{display:flex;gap:22px}
.why-item h3{font-size:18px;font-weight:800;text-transform:uppercase}
.why-item h4{font-size:14px;font-weight:700;margin:2px 0 8px}
.why-item li{list-style:none;font-size:13px;line-height:1.65;opacity:.9}

/* Blogs */
.blogs{height:440px;padding-top:40px;text-align:center}
.blog-list{display:flex;justify-content:center;gap:26px;margin-top:28px}
.blog-card{width:300px;text-align:left;box-shadow:0 2px 12px rgba(0,0,0,.12);background:var(--white)}
.blog-photo{height:160px;background:linear-gradient(135deg,#aab6c4,#5e6c7c)}
.blog-body{position:relative;padding:24px 18px 16px}
.blog-date{position:absolute;top:-13px;left:18px;background:var(--orange);color:var(--white);font-size:11px;font-weight:700;padding:4px 14px;border-radius:14px}
.blog-body h3{font-size:15px;font-weight:700;color:var(--navy)}
.blog-body p{font-size:12.5px;color:var(--muted);line-height:1.5;margin:6px 0 10px}
.read-more{font-size:12px;font-weight:700;color:var(--blue)}

/* Membership */
.membership{position:relative;height:420px;display:flex;flex-direction:column;align-items:center;justify-content:center;text-align:center;color:var(--white)}
.membership-photo{position:absolute;inset:0;background:linear-gradient(120deg,#f49a45 0%,var(--orange) 45%,var(--orange-dark) 100%)}
.membership-content{position:relative}
.membership h2{font-size:34px;font-weight:800;text-transform:uppercase}
.membership p{width:560px;margin:10px auto 0;font-size:16px;line-height:1.55}

/* Footer */
.site-footer{height:116px;padding:26px 130px 0}
.footer-row{display:flex;justify-content:space-between;align-items:center}
.footer-nav{display:flex;gap:26px;font-size:12px;font-weight:600;text-transform:uppercase;color:var(--ink)}
.social{display:flex;gap:8px}
.social span{width:26px;height:26px;border-radius:50%;background:var(--navy)}
.copyright{margin-top:14px;font-size:12px;color:var(--muted)}
</style>
</head>
<body>

<header class="site-header">
  <a class="brand" href="#"><span class="brand-dot"></span>KLOMB</a>
  <nav class="main-nav">
    <a class="active" href="#">Home</a>
    <a href="#">About Us</a>
    <a href="#">Book Titles</a>
    <a href="#">Blog</a>
    <a href="#">Membership</a>
    <a href="#">Contact Us</a>
  </nav>
</header>

<section class="hero">
  <div class="hero-photo" role="img" aria-label="Businessman touching a screen of glowing gears in a dark office"></div>
  <div class="hero-content">
    <h1>KLOMB accelerates your<br>business growth!</h1>
    <a class="btn" href="#">Learn More</a>
  </div>
</section>

<section class="about">
  <div class="about-mark"></div>
  <h2 class="section-title">About KLOMB</h2>
  <p class="about-intro">We help owners turn bold goals into steady growth through proven coaching, clear structure and practical resources built for real businesses and the teams that run them every day.</p>
  <div class="pillars">
    <article class="pillar coaching">
      <svg class="pillar-icon" width="80" height="90" viewBox="0 0 80 90"><polygon points="40,2 78,24 78,66 40,88 2,66 2,24" fill="#2f8fd8"/><circle cx="40" cy="36" r="9" fill="#fff"/><path d="M22 62c3-11 11-15 18-15s15 4 18 15z" fill="#fff"/></svg>
      <h3>Coaching</h3>
      <p>Coaching for you and your leadership team</p>
      <p>Lasting goals, monthly and quarterly touchpoints, personal coaching</p>
      <p>Individual learning needs</p>
      <p>Peer groups for growing business owners</p>
    </article>
    <article class="pillar structure">
      <svg class="pillar-icon" width="80" height="90" viewBox="0 0 80 90"><polygon points="40,2 78,24 78,66 40,88 2,66 2,24" fill="#2c9a5a"/><rect x="24" y="28" width="32" height="8" fill="#fff"/><rect x="24" y="41" width="32" height="8" fill="#fff"/><rect x="24" y="54" width="32" height="8" fill="#fff"/></svg>
      <h3>Structure</h3>
      <p>Structured program that ensures focus, productivity and accountability</p>
      <p>Proven systems to elevate, streamline and scale</p>
      <p>KLOMB Strategy Book - the clarity and alignment</p>
    </article>
    <article class="pillar resources">
      <svg class="pillar-icon" width="80" height="90" viewBox="0 0 80 90"><polygon points="40,2 78,24 78,66 40,88 2,66 2,24" fill="#f07b22"/><rect x="25" y="26" width="30" height="38" rx="2" fill="#fff"/><rect x="30" y="34" width="20" height="3" fill="#f07b22"/><rect x="30" y="42" width="20" height="3" fill="#f07b22"/><rect x="30" y="50" width="14" height="3" fill="#f07b22"/></svg>
      <h3>Resources</h3>
      <p>Pre-packaged business processes</p>
      <p>Simplified business templates and forms</p>
      <p>Online, self-paced learning library</p>
      <p>Technology platform for tracking and accountability</p>
    </article>
  </div>
</section>

<section class="why">
  <h2 class="section-title">Why we are</h2>
  <div class="why-grid">
    <div class="why-item">
      <svg width="60" height="66" viewBox="0 0 60 66"><polygon points="30,2 58,18 58,48 30,64 2,48 2,18" fill="none" stroke="#fff" stroke-width="2"/><circle cx="30" cy="33" r="12" fill="none" stroke="#fff" stroke-width="2"/><circle cx="30" cy="33" r="4" fill="#fff"/></svg>
      <div><h3>Strategy</h3><h4>Long-Term Vision, Tactical Planning</h4>
        <ul><li>Strategy Deck</li><li>Marketing Plan</li><li>Financial Plan</li><li>Operating Plan</li></ul></div>
    </div>
    <div class="why-item">
      <svg width="60" height="66" viewBox="0 0 60 66"><polygon points="30,2 58,18 58,48 30,64 2,48 2,18" fill="none" stroke="#fff" stroke-width="2"/><path d="M20 44l20-20M30 24h10v10" fill="none" stroke="#fff" stroke-width="2.5"/></svg>
      <div><h3>Action</h3><h4>Processes to Execute the Vision</h4>
        <ul><li>Operating Processes</li><li>Action Plans</li><li>Customizable Industry Processes</li></ul></div>
    </div>
    <div class="why-item">
      <svg width="60" height="66" viewBox="0 0 60 66"><polygon points="30,2 58,18 58,48 30,64 2,48 2,18" fill="none" stroke="#fff" stroke-width="2"/><path d="M20 34l7 7 14-15" fill="none" stroke="#fff" stroke-width="3"/></svg>
      <div><h3>Account Ability</h3><h4>Tools and Checklists to Stay on Track</h4>
        <ul><li>Online Tracking Tools</li><li>Targets, Tasks and Topics</li></ul></div>
    </div>
    <div class="why-item">
      <svg width="60" height="66" viewBox="0 0 60 66"><polygon points="30,2 58,18 58,48 30,64 2,48 2,18" fill="none" stroke="#fff" stroke-width="2"/><rect x="19" y="36" width="5" height="9" fill="#fff"/><rect x="27" y="29" width="5" height="16" fill="#fff"/><rect x="35" y="22" width="5" height="23" fill="#fff"/></svg>
      <div><h3>Results</h3><h4>Dashboard &amp; Metrics</h4>
        <ul><li>Weekly KPI's</li><li>Monthly Metrics</li><li>Progress Stats</li></ul></div>
    </div>
  </div>
  <a class="btn" href="#" style="margin-top:36px">Learn More</a>
</section>

<section class="blogs">
  <h2 class="section-title">Our Blogs</h2>
  <div class="blog-list">
    <article class="blog-card">
      <div class="blog-photo" role="img" aria-label="Team meeting around a table with laptops"></div>
      <div class="blog-body"><span class="blog-date">July 4, 2016</span><h3>Blog Title here</h3><p>Short summary of the post goes here to invite readers in.</p><a class="read-more" href="#">Read More</a></div>
    </article>
    <article class="blog-card">
      <div class="blog-photo" role="img" aria-label="City office buildings seen from below"></div>
      <div class="blog-body"><span class="blog-date">July 4, 2016</span><h3>Blog Title here</h3><p>Short summary of the post goes here to invite readers in.</p><a class="read-more" href="#">Read More</a></div>
    </article>
    <article class="blog-card">
      <div class="blog-photo" role="img" aria-label="Businessman working at a desk"></div>
      <div class="blog-body"><span class="blog-date">July 4, 2016</span><h3>Condition vel dolor ipsum dictum</h3><p>Short summary of the post goes here to invite readers in.</p><a class="read-more" href="#">Read More</a></div>
    </article>
  </div>
</section>

<section class="membership">
  <div class="membership-photo" role="img" aria-label="Business team collaborating at a table, tinted orange"></div>
  <div class="membership-content">
    <h2>Our Membership</h2>
    <p>Class aptent taciti sociosqu ad litora torquent per conubia nostra per inceptos hymenaeos. Proin nulla arcu nonummy.</p>
    <a class="btn" href="#">Click Here</a>
  </div>
</section>

<footer class="site-footer">
  <div class="footer-row">
    <nav class="footer-nav">
      <a href="#">Home</a><a href="#">About Us</a><a href="#">Book Titles</a><a href="#">Blog</a><a href="#">Membership</a><a href="#">Contact Us</a><a href="#">Privacy Policy</a><a href="#">Terms of Service</a>
    </nav>
    <div class="social"><span></span><span></span><span></span><span></span></div>
  </div>
  <p class="copyright">© 2016 Company Name. All right reserved.</p>
</footer>

</body>
</html>
```